Letterhead for Law Firm Harborstone Law Group

This would be for virtual letterhead, business cards, etc.

Also logo. I am happy to pay extra for that if it is a separate project.

Harborstone Law Group

482 Alder Court, Suite 730
San Francisco, California 94387

Target Market(s)

Business law services.

Industry/Entity Type

Business

Colors

Designer to choose colors to be used in the design.

```html
<!DOCTYPE html>
<html lang="en">
<head>
<meta charset="utf-8">
<title>Harborstone Law Group – Identity Set</title>
<link href="https://fonts.googleapis.com/css2?family=Jost:wght@400;500;600&family=Arimo:wght@400;700&display=swap" rel="stylesheet">
<style>
  :root{
    --navy:#253570;
    --red:#b81e27;
    --white:#ffffff;
    --stage-light:#7d7d7d;
    --stage-dark:#545454;
    --brief-text:#f0f0f0;
    --faint:#e9ebf2;
  }
  *{margin:0;padding:0;box-sizing:border-box}
  html,body{width:1200px;height:1000px;overflow:hidden}
  body{position:relative;background:linear-gradient(115deg,var(--stage-light) 0%,var(--stage-dark) 100%);font-family:"Arimo",Arial,sans-serif}
  .brief{position:absolute;left:130px;top:83px;color:var(--brief-text);font-size:19.5px;line-height:24px}
  .sheet{position:absolute;background:var(--white);overflow:hidden}
  .sheet.navy{background:var(--navy)}
  .wordmark{position:absolute;left:0;right:0;text-align:center;font-family:"Jost",sans-serif;font-weight:500;color:var(--navy);white-space:nowrap}
  .navy .wordmark{color:var(--white)}
  .mark-dot{display:block;margin:0 auto 14px;border-radius:50%;background:var(--red)}
  .stripe{position:absolute;left:0;bottom:0;width:100%}
  .faint-disc{position:absolute;border-radius:50%}
  .holder{position:absolute;font-family:"Jost",sans-serif;font-weight:600;font-size:13px;letter-spacing:.4px}
  .role{position:absolute;font-size:6px}
  .contacts{position:absolute;list-style:none;font-size:6.4px;line-height:8.9px}
  .contacts li{display:flex;align-items:flex-start;gap:4px}
  .contacts li .ico{flex:none;width:6px;height:6px;margin-top:1px;background:var(--navy);border-radius:1px}
  .navy .contacts li .ico{background:var(--white)}
  .contacts li .gap{display:block}
  .card-dark{color:var(--white)}
  .card-light{color:var(--navy)}
  .letter-address{position:absolute;right:150px;top:58px;text-align:right;font-size:7.6px;line-height:10px;font-weight:700;color:var(--navy)}
  .letter-rule{position:absolute;left:469px;top:48px;width:1px;height:42px;background:var(--navy)}
  .letter-contacts{left:477px;top:49px;color:var(--navy);font-size:7.4px;line-height:11px}
</style>
</head>
<body>

<div class="brief">
  <p>Company Name: Harborstone Law Group</p>
  <p>Logo design</p>
  <p>Business Card 2 front and 3 back Options</p>
  <p>Letterhead</p>
</div>

<!-- Logo presentation -->
<section class="sheet logo-board" style="left:130px;top:255px;width:335px;height:177px">
  <div class="wordmark" style="top:64px;font-size:27px">
    <span class="mark-dot" style="width:34px;height:34px;margin-bottom:12px"></span>
    Harborstone Law Group
  </div>
</section>

<!-- Card front, dark -->
<section class="sheet navy card-dark" style="left:18px;top:473px;width:261px;height:152px">
  <div class="faint-disc" style="left:-40px;top:30px;width:140px;height:140px;background:rgba(255,255,255,.1)"></div>
  <p class="holder" style="left:120px;top:14px">Marcus Ellery</p>
  <p class="role" style="left:120px;top:32px">CEO / Founder</p>
  <ul class="contacts" style="left:120px;top:81px">
    <li><span class="ico"></span>+0 000.481.2290</li>
    <li><span class="ico"></span>+0 000.481.2290</li>
    <li><span class="ico"></span>mail@harborstone.com</li>
    <li><span class="ico"></span>www.harborstone.com</li>
    <li><span class="ico"></span><span>482 Alder Court, Suite 730<span class="gap">San Francisco, California 94387</span></span></li>
  </ul>
</section>

<!-- Card front, light -->
<section class="sheet card-light" style="left:298px;top:473px;width:261px;height:152px">
  <div class="faint-disc" style="left:168px;top:52px;width:80px;height:80px;background:var(--red)"></div>
  <p class="holder" style="left:120px;top:12px">Marcus Ellery</p>
  <p class="role" style="left:120px;top:28px">CEO / Founder</p>
  <ul class="contacts" style="left:26px;top:77px">
    <li><span class="ico"></span>+0 000.481.2290</li>
    <li><span class="ico"></span>+0 000.481.2290</li>
    <li><span class="ico"></span>mail@harborstone.com</li>
    <li><span class="ico"></span>www.harborstonelaw.com</li>
    <li><span class="ico"></span><span>482 Alder Court, Suite 730<span class="gap">San Francisco, California 94387</span></span></li>
  </ul>
  <svg class="stripe" viewBox="0 0 261 9" height="9" preserveAspectRatio="none" aria-hidden="true">
    <polygon points="0,0 88,0 80,9 0,9" fill="var(--red)"/>
    <polygon points="95,0 261,0 261,9 87,9" fill="var(--navy)"/>
  </svg>
</section>

<!-- Card back, white -->
<section class="sheet" style="left:18px;top:642px;width:262px;height:153px">
  <div class="wordmark" style="top:32px;font-size:19px">
    <span class="mark-dot" style="width:30px;height:30px;margin-bottom:38px"></span>
    Harborstone Law Group
  </div>
</section>

<!-- Card back, navy -->
<section class="sheet navy" style="left:297px;top:642px;width:261px;height:152px">
  <div class="wordmark" style="top:28px;font-size:19px">
    <span class="mark-dot" style="width:30px;height:30px;margin-bottom:38px"></span>
    Harborstone Law Group
  </div>
</section>

<!-- Card back, white with stripe -->
<section class="sheet" style="left:297px;top:821px;width:261px;height:152px">
  <div class="wordmark" style="top:36px;font-size:19px">
    <span class="mark-dot" style="width:30px;height:30px;margin-bottom:33px"></span>
    Harborstone Law Group
  </div>
  <svg class="stripe" viewBox="0 0 261 9" height="9" preserveAspectRatio="none" aria-hidden="true">
    <polygon points="0,0 88,0 80,9 0,9" fill="var(--red)"/>
    <polygon points="95,0 261,0 261,9 87,9" fill="var(--navy)"/>
  </svg>
</section>

<!-- Letterhead -->
<section class="sheet letterhead" style="left:571px;top:182px;width:612px;height:792px">
  <div class="wordmark" style="left:41px;right:auto;top:26px;font-size:17px;text-align:left">
    <span class="mark-dot" style="width:26px;height:26px;margin:0 0 14px 76px"></span>
    Harborstone Law Group
  </div>
  <p class="letter-address">482 Alder Court, Suite 730<br>San Francisco, California 94387</p>
  <div class="letter-rule"></div>
  <ul class="contacts letter-contacts">
    <li><span class="ico"></span>+0 000.481.2290</li>
    <li><span class="ico"></span>+0 000.481.2290</li>
    <li><span class="ico"></span>mail@harborstone.com</li>
    <li><span class="ico"></span>www.harborstonelaw.com</li>
  </ul>
  <div class="faint-disc" style="left:300px;top:520px;width:260px;height:260px;background:var(--faint)"></div>
  <svg class="stripe" viewBox="0 0 612 26" height="26" preserveAspectRatio="none" aria-hidden="true">
    <polygon points="0,0 206,0 184,26 0,26" fill="var(--red)"/>
    <polygon points="222,0 612,0 612,26 200,26" fill="var(--navy)"/>
  </svg>
</section>

</body>
</html>
```